Business Card Re-Design...or logo does not look sharp

Hello

We are a start-up and just need someone to help us.

Our colors are: Marlowe Hush pink (yeah I know) and charcoal for the lettering.

I am attaching our logo which needs cleaning up.

We want the JUST the lady ironing on the table (pink) in front, and the background in charcoal. All the business info can be on the back.

Dims on card are 2 x 2''

Also, if you have better ideas....please let us know!

Thanks

Gregory

La Comadre Vapor
4827 Quellbrook Dr Suite B2
El Paso TX 79936
915-555-0148

```html
<!DOCTYPE html>
<html lang="en">
<head>
<meta charset="utf-8">
<title>La Comadre Vapor — Business Card</title>
<link rel="stylesheet" href="https://fonts.googleapis.com/css2?family=Dancing+Script:wght@400;700&family=Tinos&display=swap">
<style>
  :root {
    --charcoal: #464646;
    --charcoal-deep: #3c3c3c;
    --pink: #ee3a6e;
    --paper: #ffffff;
    --backdrop: #e4e4e4;
    --silhouette-grey: #6e6e6e;
  }
  * { margin: 0; padding: 0; box-sizing: border-box; }
  html, body {
    width: 1200px;
    height: 910px;
    overflow: hidden;
    background: var(--backdrop);
  }
  .card-sheet {
    width: 1200px;
    height: 910px;
    display: flex;
    flex-direction: column;
    align-items: center;
    justify-content: center;
    gap: 40px;
  }
  .card {
    position: relative;
    width: 700px;
    height: 400px;
    background: var(--paper);
    overflow: hidden;
    box-shadow: 0 2px 6px rgba(0,0,0,0.15);
  }
  .card-header {
    position: absolute;
    inset: 0;
    width: 700px;
    height: 400px;
  }
  .card-illustration {
    position: absolute;
  }
  .card-front .card-illustration {
    left: 45px;
    top: 190px;
    width: 235px;
    height: 185px;
    background: linear-gradient(180deg, #f0507e, var(--pink));
    border-radius: 6px;
  }
  .card-back .card-illustration {
    left: 115px;
    top: 200px;
    width: 110px;
    height: 90px;
    background: var(--silhouette-grey);
    border-radius: 4px;
  }
  .brand-name {
    position: absolute;
    font-family: "Dancing Script", cursive;
    white-space: nowrap;
  }
  .card-front .brand-name {
    left: 335px;
    top: 270px;
    font-size: 44px;
    font-weight: 400;
    color: var(--charcoal);
    line-height: 1.2;
  }
  .contact-block {
    position: absolute;
    left: 250px;
    top: 190px;
    text-align: center;
  }
  .card-back .brand-name {
    position: static;
    display: block;
    font-size: 38px;
    font-weight: 700;
    color: var(--pink);
    line-height: 1.1;
  }
  .contact-line {
    display: block;
    font-family: "Tinos", serif;
    font-size: 22px;
    color: var(--charcoal);
    line-height: 1.2;
  }
</style>
</head>
<body>
<main class="card-sheet">

  <section class="card card-front" aria-label="Card front">
    <svg class="card-header" viewBox="0 0 700 400">
      <defs>
        <linearGradient id="front-band-tone" x1="0" y1="0" x2="0" y2="1">
          <stop offset="0" stop-color="var(--charcoal-deep)"/>
          <stop offset="1" stop-color="var(--charcoal)"/>
        </linearGradient>
      </defs>
      <path d="M0,0 H700 V195 C600,190 500,150 420,140 C390,136 380,110 330,108 C230,104 130,125 0,115 Z"
            fill="url(#front-band-tone)" role="img" aria-label="Charcoal band with white polka dot pattern"/>
      <path d="M0,115 C130,125 230,104 330,108 C380,110 390,136 420,140 C500,150 600,190 700,195"
            fill="none" stroke="var(--paper)" stroke-width="7"/>
      <path d="M0,123 C130,133 230,112 330,116 C380,118 390,144 420,148 C500,158 600,198 700,203 V230 C600,226 500,185 420,175 C380,170 370,145 325,144 C230,140 130,160 0,160 Z"
            fill="var(--pink)"/>
    </svg>
    <div class="card-illustration" role="img" aria-label="Pink silhouette of a woman ironing at a table"></div>
    <h1 class="brand-name">La Comadre Vapor</h1>
  </section>

  <section class="card card-back" aria-label="Card back">
    <svg class="card-header" viewBox="0 0 700 400">
      <defs>
        <linearGradient id="back-band-tone" x1="0" y1="0" x2="0" y2="1">
          <stop offset="0" stop-color="var(--charcoal-deep)"/>
          <stop offset="1" stop-color="var(--charcoal)"/>
        </linearGradient>
      </defs>
      <path d="M0,0 H700 V150 C610,145 560,105 470,100 C400,96 380,72 320,72 C230,72 140,112 0,100 Z"
            fill="url(#back-band-tone)" role="img" aria-label="Charcoal band with white polka dot pattern"/>
      <path d="M0,100 C140,112 230,72 320,72 C380,72 400,96 470,100 C560,105 610,145 700,150"
            fill="none" stroke="var(--paper)" stroke-width="6"/>
      <path d="M0,107 C140,119 230,79 320,79 C380,79 400,103 470,107 C560,112 610,152 700,157 V180 C610,176 560,135 470,130 C400,126 380,102 320,102 C230,102 140,140 0,140 Z"
            fill="var(--pink)"/>
    </svg>
    <div class="card-illustration" role="img" aria-label="Small grey silhouette of a woman ironing at a table"></div>
    <div class="contact-block">
      <h2 class="brand-name">La Comadre Vapor</h2>
      <span class="contact-line">4827 Quellbrook Dr. Ste. B2</span>
      <span class="contact-line">El Paso, TX 79936</span>
      <span class="contact-line">915-555-0148</span>
    </div>
  </section>

</main>
</body>
</html>
```